Adventure Flights/ Private Charters (Air Taxi)

Toronto's newest Air Taxi "Northlake Skyways"
www.SOARNLS.example
instagram @iSoarNLS

We are operating light twin engine aircraft based out of downtown Toronto. Will be attacking 2 markets.
1. Tourism (adventure/sightseeing/champagne flights), day trips to destinations such as Niagara Falls, Muskoka
2. Short haul business travel as an on demand air taxi service. Our services will make possible private flying at affordable prices. Target is executives of medium sized companies travelling within 300 miles (500 km) of Toronto.

Seating arrangement is 4 passenger executive.

We are open to any bold or catchy statements. We would like to use our theme colours of blue, grey, and possibly black (can be seen on the logo on our website) and have logos and pictures to include.

pictures can be extracted from website, or shared once winning design is selected

Target Market(s)

tourism, executives

Industry/Entity Type

Taxi

Font styles to use
Sans Serif

Requirements
Must have
• refer to website for basic info.
• 3 FOLD ONLY PLEASE

```html
<!DOCTYPE html>
<html lang="en">
<head>
<meta charset="utf-8">
<title>Northlake Skyways – Tri-fold Brochure</title>
<link href="https://fonts.googleapis.com/css2?family=Open+Sans:wght@400;600;700;800&family=Roboto+Condensed:wght@400;700&display=swap" rel="stylesheet">
<style>
  :root{
    --blue:#1f6fc4;
    --blue-deep:#15559c;
    --blue-light:#d6e6f7;
    --ink:#2f343b;
    --grey:#6c737c;
    --grey-light:#e8ebee;
    --rule:#cfd5db;
    --paper:#ffffff;
    --page:#e4e6e9;
  }
  *{box-sizing:border-box;margin:0;padding:0}
  html,body{width:855px;height:1200px;overflow:hidden;background:var(--page)}
  body{font-family:"Open Sans",sans-serif;color:var(--ink);position:relative}
  .sheet{position:absolute;left:20px;width:815px;background:var(--paper);box-shadow:0 2px 6px rgba(0,0,0,.18);overflow:hidden}
  .sheet--outside{top:18px;height:545px}
  .sheet--inside{top:590px;height:592px}
  .panel{position:absolute;top:0;height:100%;width:271.6px}
  .panel--1{left:0}.panel--2{left:271.6px}.panel--3{left:543.2px}
  .photo{position:absolute}
  .blue-panel{background:var(--blue);color:#fff}
  h2{font-family:"Roboto Condensed",sans-serif;font-weight:700;text-transform:uppercase;letter-spacing:.3px}
  .body-copy{font-size:7.6px;line-height:1.5}

  /* outside sheet */
  .adv-title{position:absolute;left:16px;top:20px;font-size:17px;color:#fff}
  .adv-copy{position:absolute;left:16px;top:46px;width:240px}
  .adv-copy p+p{margin-top:6px}
  .tours-title{position:absolute;left:16px;top:326px;font-size:10px;color:#fff}
  .tours-list{position:absolute;left:16px;top:344px;width:240px;list-style:none;font-size:7.8px;line-height:1.55}
  .tours-list li{padding-left:10px;position:relative;margin-bottom:3px}
  .tours-list li::before{content:"";position:absolute;left:0;top:4px;width:4px;height:4px;background:#fff;border-radius:50%}

  .contact-tab{position:absolute;left:18px;top:14px;background:var(--blue);color:#fff;font-size:12px;padding:4px 14px}
  .contact-lines{position:absolute;left:18px;top:44px;list-style:none;font-size:7.8px;line-height:1.5}
  .contact-lines li{display:flex;align-items:flex-start;gap:6px;margin-bottom:4px}
  .contact-lines svg{flex:none;margin-top:1px}

  .brand{position:absolute;left:0;right:0;top:30px;text-align:center}
  .brand-name{display:inline-flex;align-items:center;gap:8px;font-family:"Roboto Condensed",sans-serif;font-weight:700;font-size:19px;color:var(--blue-deep);text-transform:uppercase}
  .brand-dot{width:12px;height:12px;border-radius:50%;background:var(--blue)}
  .cover-tagline{position:absolute;right:18px;top:418px;text-align:right;line-height:1}
  .cover-tagline .l1{font-size:18px;color:var(--ink)}
  .cover-tagline .l2{font-size:36px;color:var(--blue);margin-top:4px}

  /* inside sheet */
  .feature{position:absolute;left:16px;width:244px;display:flex;gap:10px}
  .feature-icon{flex:none;width:30px;height:30px;border-radius:50%;border:1.5px solid #fff;display:flex;align-items:center;justify-content:center}
  .feature h3{font-family:"Roboto Condensed",sans-serif;font-size:10px;text-transform:uppercase;margin-bottom:3px}
  .web-foot{position:absolute;left:0;right:0;bottom:12px;text-align:center;font-size:9px;font-weight:600;letter-spacing:.5px}

  .fly-title{position:absolute;left:282px;top:26px;line-height:1.05;color:var(--blue)}
  .fly-title .l1{font-size:18px}
  .fly-title .l2{font-size:28px}
  .fly-copy{position:absolute;left:282px;top:100px;width:240px;color:var(--grey)}

  .fares{position:absolute;left:282px;top:232px;width:516px;border-collapse:collapse;font-size:7.6px}
  .fares th{background:var(--blue);color:#fff;font-family:"Roboto Condensed",sans-serif;font-weight:700;text-transform:uppercase;padding:5px 4px;text-align:left}
  .fares td{padding:4px 4px;border-bottom:1px solid var(--rule)}
  .fares tr:nth-child(even) td{background:var(--grey-light)}
  .fares td.num{text-align:center}
  .fares th.num{text-align:center}
  .fare-note{position:absolute;left:271.6px;right:0;bottom:0;height:22px;background:var(--blue);color:#fff;font-size:7.6px;display:flex;align-items:center;justify-content:flex-end;padding-right:16px;font-style:italic}
</style>
</head>
<body>

<!-- OUTSIDE -->
<section class="sheet sheet--outside">
  <div class="panel panel--1 blue-panel">
    <h2 class="adv-title">Adventure Flying</h2>
    <div class="adv-copy body-copy">
      <p>Looking for something new and exciting in Toronto? Let your city from a whole new perspective.</p>
      <p>Introducing private scenic air tours: a quiet, smooth ride in a light twin with panoramic windows, a skilled pilot and only your party on board. Choose a sunset loop over the lake, a champagne flight above the skyline or a day trip to the falls and cottage country.</p>
      <p>Our adventure flights leave from downtown Toronto, so you spend less time on the road and more time in the air. Ask about gift cards for birthdays and anniversaries.</p>
    </div>
    <div class="photo" role="img" aria-label="Photo of the Toronto waterfront and island from the air" style="left:16px;top:190px;width:240px;height:122px;background:linear-gradient(160deg,#9fc3e4,#5d8fb8 55%,#3f6b4f)"></div>
    <h2 class="tours-title">Adventure tours starting at $99/person</h2>
    <ul class="tours-list">
      <li>Toronto Skyline Tour – 30 minutes over downtown</li>
      <li>Toronto and Niagara Falls – a full loop with views of the gorge</li>
      <li>Toronto and Muskoka – lakes, islands and cottage country</li>
      <li>Sunset Champagne Flight – evening loop for two</li>
    </ul>
  </div>

  <div class="panel panel--2">
    <h2 class="contact-tab">Contact Us</h2>
    <ul class="contact-lines">
      <li>
        <svg width="9" height="11" viewBox="0 0 9 11"><path d="M4.5 0A4.5 4.5 0 0 0 0 4.5C0 7.8 4.5 11 4.5 11S9 7.8 9 4.5A4.5 4.5 0 0 0 4.5 0Z" fill="var(--blue)"/><circle cx="4.5" cy="4.3" r="1.6" fill="#fff"/></svg>
        <span>Hangar 4, Suite 210<br>1 Harbour Field Road<br>Toronto, Ontario M0X 0X0</span>
      </li>
      <li>
        <svg width="10" height="10" viewBox="0 0 10 10"><path d="M2 0.5 3.8 2.6 2.8 4a6 6 0 0 0 3.2 3.2l1.4-1L9.5 8 8.4 9.5C4 9.5.5 6 .5 1.6Z" fill="var(--blue)"/></svg>
        <span>+1 555 010 4477</span>
      </li>
      <li>
        <svg width="10" height="10" viewBox="0 0 10 10"><circle cx="5" cy="5" r="4.3" fill="none" stroke="var(--blue)" stroke-width="1.1"/><path d="M.7 5h8.6M5 .7c-2.4 2.6-2.4 6 0 8.6M5 .7c2.4 2.6 2.4 6 0 8.6" fill="none" stroke="var(--blue)" stroke-width=".8"/></svg>
        <span>www.SOARNLS.example</span>
      </li>
    </ul>
    <div class="photo" role="img" aria-label="Map of the Toronto area showing the downtown airfield" style="left:18px;top:122px;width:236px;height:168px;background:linear-gradient(135deg,#eef1e9,#d9e6d2 50%,#b9d3ea)"></div>
    <div class="photo" role="img" aria-label="Photo of the Toronto skyline across the harbour" style="left:0;top:310px;width:271.6px;height:235px;background:linear-gradient(180deg,#a9cbe9,#7ea8cf 55%,#476b8c)"></div>
  </div>

  <div class="panel panel--3">
    <div class="brand"><span class="brand-name"><span class="brand-dot"></span>Northlake Skyways</span></div>
    <div class="photo" role="img" aria-label="Photo of a light twin-engine aircraft flying over the city" style="left:0;top:90px;width:271.6px;height:300px;background:linear-gradient(170deg,#bcd7ef,#6f9fcc 60%,#3d5f80)"></div>
    <svg class="photo" style="left:0;top:380px" width="272" height="40" viewBox="0 0 272 40"><path d="M0 10 272 0V14L0 40Z" fill="var(--grey-light)"/><path d="M0 10 272 0V4L0 16Z" fill="var(--blue)"/></svg>
    <h2 class="cover-tagline"><div class="l1">Toronto's New</div><div class="l2">Air Taxi</div></h2>
  </div>
</section>

<!-- INSIDE -->
<section class="sheet sheet--inside">
  <div class="panel panel--1 blue-panel">
    <div class="photo" role="img" aria-label="Photo of the aircraft cabin and wing over the lake" style="left:0;top:0;width:271.6px;height:200px;background:linear-gradient(160deg,#cfe0f0,#8fb3d6 55%,#4f7aa5)"></div>

    <div class="feature" style="top:222px">
      <span class="feature-icon"><svg width="16" height="14" viewBox="0 0 16 14"><rect x="1" y="4" width="14" height="9" rx="1" fill="none" stroke="#fff" stroke-width="1.4"/><path d="M5.5 4V2h5v2" fill="none" stroke="#fff" stroke-width="1.4"/></svg></span>
      <div><h3>VIP Business Travel</h3><p class="body-copy">Fast, private flights to regional cities without airport lines. Fly out in the morning and be home for dinner the same day.</p></div>
    </div>
    <div class="feature" style="top:302px">
      <span class="feature-icon"><svg width="14" height="16" viewBox="0 0 14 16"><path d="M3 1h5l1 8H3Z M2 10h10v2H2Z M3 12v3M11 12v3" fill="none" stroke="#fff" stroke-width="1.4"/></svg></span>
      <div><h3>Executive Class Seating</h3><p class="body-copy">Four passenger executive seating, leather finish and room to work. Your team travels together in comfort.</p></div>
    </div>
    <div class="feature" style="top:382px">
      <span class="feature-icon"><svg width="16" height="16" viewBox="0 0 16 16"><circle cx="8" cy="8" r="6.3" fill="none" stroke="#fff" stroke-width="1.4"/><path d="M8 4v4l3 2" fill="none" stroke="#fff" stroke-width="1.4"/></svg></span>
      <div><h3>Saves You Time</h3><p class="body-copy">Depart minutes from downtown and land close to where you need to be. Less driving, less waiting, more done.</p></div>
    </div>
    <p class="web-foot">www.SOARNLS.example</p>
  </div>

  <div class="photo" role="img" aria-label="Photo of the twin-engine aircraft parked on the apron" style="left:282px;top:0;width:0;height:0"></div>
  <div class="photo" role="img" aria-label="Photo of the twin-engine aircraft on the runway" style="left:543.2px;top:0;width:271.8px;height:215px;background:linear-gradient(160deg,#dbe7f3,#a4bfd9 55%,#5f7c97)"></div>

  <h2 class="fly-title"><div class="l1">Fly Private for</div><div class="l2">$6/KM</div></h2>
  <p class="fly-copy body-copy">Air taxi travel is more than a luxury: it is a smart choice for business and personal trips. With our light twin you can reach regional airports across Ontario at a fair, simple price per kilometre.</p>

  <table class="fares">
    <thead>
      <tr><th>From</th><th>To</th><th class="num">NM</th><th class="num">Time</th><th class="num">Price (USD)</th><th class="num">Round Trip</th></tr>
    </thead>
    <tbody>
      <tr><td>CYTZ (Toronto Island)</td><td>CYSN (St. Catharines)</td><td class="num">28</td><td class="num">0:21</td><td class="num">$300</td><td class="num">$600</td></tr>
      <tr><td>CYTZ (Toronto Island)</td><td>CYOO (Oshawa)</td><td class="num">26</td><td class="num">0:20</td><td class="num">$300</td><td class="num">$600</td></tr>
      <tr><td>CYTZ (Toronto Island)</td><td>CYHM (Hamilton)</td><td class="num">34</td><td class="num">0:27</td><td class="num">$325</td><td class="num">$650</td></tr>
      <tr><td>CYTZ (Toronto Island)</td><td>CYKF (Waterloo)</td><td class="num">54</td><td class="num">0:32</td><td class="num">$400</td><td class="num">$800</td></tr>
      <tr><td>CYTZ (Toronto Island)</td><td>CYLS (Barrie)</td><td class="num">52</td><td class="num">0:32</td><td class="num">$500</td><td class="num">$1000</td></tr>
      <tr><td>CYTZ (Toronto Island)</td><td>CYPQ (Peterborough)</td><td class="num">72</td><td class="num">0:38</td><td class="num">$600</td><td class="num">$1200</td></tr>
      <tr><td>CYTZ (Toronto Island)</td><td>CYXU (London)</td><td class="num">86</td><td class="num">0:40</td><td class="num">$700</td><td class="num">$1400</td></tr>
      <tr><td>CYTZ (Toronto Island)</td><td>CYQA (Muskoka)</td><td class="num">81</td><td class="num">0:40</td><td class="num">$700</td><td class="num">$1400</td></tr>
      <tr><td>CYTZ (Toronto Island)</td><td>CYQG (Windsor)</td><td class="num">188</td><td class="num">1:12</td><td class="num">$1,500</td><td class="num">$3,000</td></tr>
      <tr><td>CYTZ (Toronto Island)</td><td>CYOW (Ottawa)</td><td class="num">196</td><td class="num">1:15</td><td class="num">$1,600</td><td class="num">$3,200</td></tr>
      <tr><td>CYTZ (Toronto Island)</td><td>CYSB (Sudbury)</td><td class="num">180</td><td class="num">1:10</td><td class="num">$1,450</td><td class="num">$2,900</td></tr>
      <tr><td>CYTZ (Toronto Island)</td><td>CYUL (Montreal)</td><td class="num">270</td><td class="num">1:45</td><td class="num">$2,200</td><td class="num">$4,400</td></tr>
      <tr><td>CYTZ (Toronto Island)</td><td>CYYB (North Bay)</td><td class="num">155</td><td class="num">1:02</td><td class="num">$1,250</td><td class="num">$2,500</td></tr>
      <tr><td>CYTZ (Toronto Island)</td><td>CYGK (Kingston)</td><td class="num">132</td><td class="num">0:55</td><td class="num">$1,050</td><td class="num">$2,100</td></tr>
    </tbody>
  </table>
  <p class="fare-note">All prices do not include taxes and are subject to change without notice.</p>
</section>

</body>
</html>
```